Strategy and Technology Consulting - Our Story and Values Page

Interior Page design – Our History and Our Values

Our homepage has been designed and we are looking for a design for one of the interior pages. This interior page tells the story of Our History and Our Values

Because the homepage has been designed, we would like this interior page to reflect the design of the homepage without being a mirror image of the homepage.

This site will be implemented in WordPress using the Elementor framework.

Font: Poppins medium and Poppins dark
Illustrations: Our homepage illustrations were designed by “Teslo 1964” on Imagevale. Compatible original or stock illustrations are welcome. Stock photography is also welcome. Teslo is also available through Teslo Bramen on Portvue

• Homepage design – this is the design we will use for our homepage. Contest entries should reflect this basic style but should be distinctly different from the homepage.
• Our History and Our Values – Wireframe – the basic layout of the page we are looking for.
• Our History and Our Values – Word document with the text supporting the wireframe.
• Color Palette – please use colors compatible with the palette attached.

Our Story - timeline
There is a timeline element in the wireframe. The wireframe displays this as a series of chevrons (arrows), but it does not need to be. Creativity in display of the timeline is appreciated.

Our Values
If you look at the Word document, you will see that there are a lot of words on the page. The winning design will present the information in a way that engages the user without overwhelming them with too much to read. For example, they may click on a value and see more information.

Target Market(s)

CIO's and Technology Executives

Number of Pages Required

1 page

Font styles to use
Sans Serif
Other font styles liked:
• Poppin

Requirements
Must have
• A timeline element, all of our values
Nice to have
• Clever timeline display

```html
<!DOCTYPE html>
<html lang="en">
<head>
<meta charset="utf-8">
<title>Vantrix – Our Story and Values</title>
<link href="https://fonts.googleapis.com/css2?family=Poppins:wght@400;500;600;700;800&display=swap" rel="stylesheet">
<style>
:root{
  --page-bg:#eef0f3;
  --frame-bg:#fafafa;
  --navy:#3f4a5f;
  --navy-dark:#343e51;
  --blue:#2b679d;
  --blue-mid:#4a86bb;
  --blue-light:#b9daf0;
  --blue-pale:#dbeaf5;
  --slate:#a3b7c6;
  --slate-dark:#8ea4b5;
  --sky:#b7d9ef;
  --sky-dark:#9ec7e3;
  --yellow:#e8b42c;
  --yellow-dark:#d39f17;
  --text:#3a4354;
  --muted:#7b8494;
  --white:#ffffff;
}
*{margin:0;padding:0;box-sizing:border-box}
html,body{width:1200px;height:4173px;overflow:hidden}
body{background:var(--page-bg);font-family:'Poppins',sans-serif;color:var(--text);position:relative}
.frame{position:absolute;left:94px;width:1023px;background:var(--frame-bg);box-shadow:0 20px 60px rgba(40,50,70,.18);overflow:hidden}
.frame-story{top:32px;height:1992px}
.frame-values{top:2050px;height:2024px}

/* header */
.site-header{position:absolute;top:0;left:0;right:0;height:81px;background:var(--white);display:flex;align-items:center}
.brand{position:absolute;left:76px;top:20px;font-size:38px;font-weight:500;color:#7d8797;letter-spacing:-.5px;display:flex;align-items:center;gap:8px}
.brand-dot{width:12px;height:12px;border-radius:50%;background:var(--yellow)}
.main-nav{position:absolute;left:464px;top:31px;display:flex;gap:22px;font-size:11px;font-weight:600;color:var(--navy)}
.main-nav .home{width:12px;height:12px}
.btn-contact{position:absolute;left:835px;top:25px;width:111px;height:30px;border-radius:15px;background:var(--yellow);color:var(--white);font-size:10px;font-weight:700;display:flex;align-items:center;justify-content:center}

/* story */
.story-title{position:absolute;left:76px;top:140px;font-size:48px;font-weight:800;color:var(--navy)}
.story-band{position:absolute;left:0;top:0;width:1023px;height:620px}
.year{position:absolute;width:110px;height:110px;border-radius:50%;background:var(--white);display:flex;align-items:center;justify-content:center;text-align:center;font-size:14px;font-weight:700;color:var(--yellow);line-height:1.4}
.milestones{position:absolute;list-style:none;font-size:12px;color:var(--white);line-height:1.5}
.milestones li{position:relative;padding-left:16px;margin-bottom:10px}
.milestones li::before{content:"";position:absolute;left:0;top:5px;width:9px;height:9px;border-radius:50%;background:var(--yellow)}
.milestones li.sub{padding-left:28px;margin-bottom:6px}
.milestones li.sub::before{left:16px;top:7px;width:5px;height:5px;background:var(--white)}

/* values */
.section-title{position:absolute;left:0;right:0;text-align:center;font-size:27px;font-weight:800;color:var(--navy)}
.values{position:absolute;left:222px;width:578px}
.value-head{height:50px;border-radius:6px;display:flex;align-items:center;color:var(--white);font-size:12px;font-weight:700;position:relative;overflow:hidden;margin-bottom:4px}
.value-num{width:60px;padding-left:16px}
.value-name{flex:1;text-align:center;padding-right:60px}
.value-icon{position:absolute;right:0;top:0;width:59px;height:50px;display:flex;align-items:center;justify-content:center}
.v-dark{background:var(--navy)} .v-dark .value-icon{background:var(--navy-dark)}
.v-slate{background:var(--slate)} .v-slate .value-icon{background:var(--slate-dark)}
.v-sky{background:var(--sky)} .v-sky .value-icon{background:var(--sky-dark)}
.v-yellow{background:var(--yellow)} .v-yellow .value-icon{background:var(--yellow-dark)}
.value-body{background:#f0f2f5;border-radius:0 0 6px 6px;display:flex;align-items:center;padding:0 40px;gap:36px;margin-top:-4px;margin-bottom:4px}
.value-art{width:210px;height:180px;border-radius:8px;flex:none;background:linear-gradient(135deg,#d8e4f0,#9fb8d6 60%,#3f5d8f)}
.value-text h3{font-size:21px;font-weight:800;color:var(--navy);line-height:1.3;margin-bottom:12px}
.value-text p{font-size:11.5px;line-height:1.5;color:var(--muted)}

/* newsletter + footer */
.footer-wave{position:absolute;left:0;top:1350px;width:1023px;height:642px}
.newsletter{position:absolute;left:116px;top:1389px;width:789px;height:175px;border-radius:88px;background:var(--yellow);display:flex;align-items:center;padding:0 68px;color:var(--white)}
.newsletter h2{font-size:27px;font-weight:800;margin-bottom:12px}
.newsletter p{font-size:12px;line-height:1.35;width:380px}
.subscribe{margin-left:auto;width:274px;height:38px;border-radius:19px;background:var(--white);display:flex;align-items:center;padding:0 4px 0 18px;font-size:10.5px;color:#9aa2ae;gap:8px}
.subscribe .go{margin-left:auto;width:32px;height:32px;border-radius:50%;background:var(--slate-dark);display:flex;align-items:center;justify-content:center}
.footer-brand{position:absolute;left:100px;top:1715px;font-size:54px;font-weight:500;color:var(--white);display:flex;align-items:center;gap:10px}
.footer-brand .brand-dot{width:14px;height:14px}
.socials{position:absolute;left:150px;top:1786px;display:flex;gap:10px}
.socials span{width:34px;height:34px;border-radius:50%;background:rgba(255,255,255,.2)}
.footer-btn{position:absolute;left:183px;top:1855px;width:111px;height:32px;border-radius:16px;background:var(--yellow);color:var(--white);font-size:10px;font-weight:700;display:flex;align-items:center;justify-content:center}
.footer-col{position:absolute;top:1700px;color:var(--white)}
.footer-col h4{font-size:16px;font-weight:700;margin-bottom:14px}
.footer-col ul{list-style:none;font-size:11px;line-height:2.45;color:#e3e7ee}
.footer-col li::before{content:"›";margin-right:8px}
.contact li::before{content:none}
.contact li{display:flex;gap:10px;line-height:1.4;margin-bottom:14px}
.contact svg{flex:none;margin-top:2px}
.copyright{position:absolute;left:0;right:0;top:1943px;height:49px;background:rgba(40,48,62,.55);color:var(--white);font-size:11px;display:flex;align-items:center;justify-content:center}
.chat{position:absolute;left:969px;top:1923px;width:40px;height:40px;border-radius:50%;background:var(--yellow);display:flex;align-items:center;justify-content:center}
</style>
</head>
<body>

<section class="frame frame-story">
  <header class="site-header">
    <div class="brand"><span class="brand-dot"></span>Vantrix</div>
    <nav class="main-nav">
      <svg class="home" viewBox="0 0 12 12"><path d="M1 6 6 1l5 5v5H7V8H5v3H1z" fill="#a3acb8"/></svg>
      <span>ABOUT US ⌄</span><span>SERVICES ⌄</span><span>INSIGHTS ⌄</span><span>JOIN US ⌄</span>
    </nav>
    <div class="btn-contact">CONTACT US</div>
  </header>

  <h1 class="story-title">Our Story</h1>

  <svg class="story-band" viewBox="0 0 1023 620" aria-hidden="true">
    <defs>
      <linearGradient id="band" x1="0" y1="1" x2="1" y2="0">
        <stop offset="0" stop-color="#22609a"/><stop offset="1" stop-color="#5a93c3"/>
      </linearGradient>
    </defs>
    <circle cx="141" cy="356" r="74" fill="var(--blue-light)"/>
    <circle cx="427" cy="287" r="74" fill="var(--blue-light)"/>
    <circle cx="674" cy="206" r="74" fill="var(--blue-light)"/>
    <path d="M0 520 C300 480 700 420 1023 470 L1023 560 C800 480 400 520 0 560Z" fill="var(--blue-pale)"/>
    <path d="M0 351 C120 320 250 300 330 283 C450 258 560 240 715 186 C820 160 920 165 1023 178 L1023 494 C900 470 780 475 553 502 C380 522 200 560 0 567Z" fill="url(#band)"/>
    <g fill="none" stroke="#fff" stroke-width="1.3" stroke-dasharray="2 3">
      <path d="M141 411 Q150 430 210 430"/><path d="M427 342 Q440 344 490 344"/><path d="M674 261 Q690 262 735 262"/>
    </g>
    <g fill="#fff"><path d="M210 426l6 4-6 4z"/><path d="M490 340l6 4-6 4z"/><path d="M735 258l6 4-6 4z"/></g>
  </svg>
  <div class="year" style="left:86px;top:301px">2017 – 2019</div>
  <div class="year" style="left:372px;top:232px">2020 – 2021</div>
  <div class="year" style="left:619px;top:151px">2022 and<br>Onward</div>

  <ul class="milestones" style="left:230px;top:390px;width:260px">
    <li>Growth Strategy Focus</li>
    <li>Consistent, Modest Growth</li>
    <li>Preliminary Focus on Technology</li>
    <li><b>Eureka!</b> Implementing strategy is hard.</li>
  </ul>
  <ul class="milestones" style="left:505px;top:296px;width:220px">
    <li>Pandemic Pauses Growth</li>
    <li>Rethinking :</li>
    <li class="sub">the business model</li>
    <li class="sub">the delivery model</li>
  </ul>
  <ul class="milestones" style="left:753px;top:216px;width:200px">
    <li>Leadership Team for Focus on Essential Areas</li>
    <li>Rapid Growth</li>
    <li>Customer Success</li>
  </ul>

  <h2 class="section-title" style="top:618px">Our Values</h2>
  <div class="values" style="top:684px">
    <div class="value-head v-dark"><span class="value-num">01.</span><span class="value-name">The Value of Every Human. Regardless.</span><span class="value-icon"><svg width="24" height="24" viewBox="0 0 24 24" fill="none" stroke="#fff" stroke-width="1.3"><circle cx="12" cy="9" r="4"/><path d="M4 21c1-5 15-5 16 0"/></svg></span></div>
    <div class="value-body" style="height:266px">
      <div class="value-art" role="img" aria-label="Illustration of a person launching a paper plane"></div>
      <div class="value-text"><h3>The Value of Every<br>Human. Regardless.</h3>
      <p>Each person's unique experiences and perspectives add vibrant hues to the tapestry of our shared existence. In a world where diversity paints the canvas of humanity, true beauty is found in recognizing the inherent and incalculable value of every human being.</p></div>
    </div>
    <div class="value-head v-slate"><span class="value-num">02.</span><span class="value-name">Collaboration</span><span class="value-icon"><svg width="24" height="24" viewBox="0 0 24 24" fill="none" stroke="#fff" stroke-width="1.3"><circle cx="8" cy="8" r="3"/><circle cx="16" cy="16" r="3"/><path d="M10 10l4 4"/></svg></span></div>
    <div class="value-head v-sky"><span class="value-num">03.</span><span class="value-name">Passion</span><span class="value-icon"><svg width="24" height="24" viewBox="0 0 24 24" fill="none" stroke="#fff" stroke-width="1.3"><path d="M12 20s-7-4-7-10a4 4 0 0 1 7-2 4 4 0 0 1 7 2c0 6-7 10-7 10z"/></svg></span></div>
    <div class="value-head v-yellow"><span class="value-num">04.</span><span class="value-name">Excellence</span><span class="value-icon"><svg width="24" height="24" viewBox="0 0 24 24" fill="none" stroke="#fff" stroke-width="1.3"><path d="M12 3l3 6 6 1-4.5 4 1 6L12 17l-5.5 3 1-6L3 10l6-1z"/></svg></span></div>
    <div class="value-head v-slate"><span class="value-num">05.</span><span class="value-name">Tenacity</span><span class="value-icon"><svg width="24" height="24" viewBox="0 0 24 24" fill="none" stroke="#fff" stroke-width="1.3"><circle cx="12" cy="12" r="7"/><path d="M12 8v4l3 2"/></svg></span></div>
    <div class="value-head v-sky"><span class="value-num">06.</span><span class="value-name">Solution Mindset</span><span class="value-icon"><svg width="24" height="24" viewBox="0 0 24 24" fill="none" stroke="#fff" stroke-width="1.3"><circle cx="12" cy="10" r="5"/><path d="M10 18h4M10 21h4"/></svg></span></div>
    <div class="value-head v-dark"><span class="value-num">07.</span><span class="value-name">Generosity</span><span class="value-icon"><svg width="24" height="24" viewBox="0 0 24 24" fill="none" stroke="#fff" stroke-width="1.3"><rect x="5" y="10" width="14" height="10"/><path d="M4 7h16v3H4zM12 7v13"/></svg></span></div>
  </div>

  <svg class="footer-wave" viewBox="0 0 1023 642" aria-hidden="true">
    <defs><linearGradient id="foot" x1="0" y1="1" x2="1" y2="0"><stop offset="0" stop-color="#5d7492"/><stop offset="1" stop-color="#3a475d"/></linearGradient></defs>
    <path d="M0 55 C100 70 180 180 300 250 C420 310 480 205 560 240 C660 285 720 300 800 250 C880 200 930 130 1023 40 L1023 642 L0 642Z" fill="#d5dbe2"/>
    <path d="M0 40 C100 55 180 165 300 232 C420 295 480 190 560 225 C660 270 720 285 800 235 C880 185 930 115 1023 25 L1023 642 L0 642Z" fill="url(#foot)"/>
  </svg>
  <div class="newsletter">
    <div><h2>Subscribe Our Newsletter</h2><p>Subscribe our newsletter to receive the latest news and exclusive offers every week, No spam.</p></div>
    <div class="subscribe"><svg width="12" height="10" viewBox="0 0 12 10"><rect x=".5" y=".5" width="11" height="9" fill="none" stroke="#9aa2ae"/><path d="M.5 .5 6 5l5.5-4.5" fill="none" stroke="#9aa2ae"/></svg>Enter email address<span class="go"><svg width="12" height="12" viewBox="0 0 12 12"><path d="M1 6 11 1 7 11 6 7z" fill="#fff"/></svg></span></div>
  </div>
  <div class="footer-brand"><span class="brand-dot"></span>Vantrix</div>
  <div class="socials"><span></span><span></span><span></span><span></span></div>
  <div class="footer-btn">CONTACT US</div>
  <div class="footer-col" style="left:418px"><h4>Quick links</h4><ul><li>Home</li><li>About Us</li><li>Services</li><li>Insights</li><li>Join Us</li><li>Contact Us</li></ul></div>
  <div class="footer-col" style="left:570px"><h4>Our Services</h4><ul><li>Business Transformation</li><li>ERP Implementations</li><li>ERP Solutions</li><li>BI and Data</li><li>Building the Right Team...</li></ul></div>
  <div class="footer-col contact" style="left:766px"><h4>Contact info</h4><ul>
    <li><svg width="12" height="10" viewBox="0 0 12 10"><rect width="12" height="10" fill="var(--yellow)"/></svg><span>Email:<br>hello@vantrixgroup.com</span></li>
    <li><svg width="12" height="12" viewBox="0 0 12 12"><path d="M2 1l3 0 1 3-2 1c1 2 2 3 4 4l1-2 3 1v3C6 11 1 6 2 1z" fill="var(--yellow)"/></svg><span>Phone:<br>+44 100 555 0142</span></li>
    <li><svg width="10" height="13" viewBox="0 0 10 13"><path d="M5 13S0 7 0 5a5 5 0 0 1 10 0c0 2-5 8-5 8z" fill="var(--yellow)"/><circle cx="5" cy="5" r="2" fill="#4a5870"/></svg><span>Location:<br>Some address line goes<br>here city name</span></li>
  </ul></div>
  <div class="copyright">© Vantrix Design 2023, All Rights Reserved</div>
  <div class="chat"><svg width="20" height="18" viewBox="0 0 20 18"><path d="M2 2h16v10H8l-4 4v-4H2z" fill="none" stroke="#fff" stroke-width="1.8"/></svg></div>
</section>

<section class="frame frame-values">
  <h2 class="section-title" style="top:34px">Our Values</h2>
  <div class="values" style="top:95px">
    <div class="value-head v-slate"><span class="value-num">02.</span><span class="value-name">Collaboration</span><span class="value-icon"><svg width="24" height="24" viewBox="0 0 24 24" fill="none" stroke="#fff" stroke-width="1.3"><circle cx="8" cy="8" r="3"/><circle cx="16" cy="16" r="3"/><path d="M10 10l4 4"/></svg></span></div>
    <div class="value-body" style="height:267px">
      <div class="value-art" role="img" aria-label="Illustration of two colleagues shaking hands across desks"></div>
      <div class="value-text"><h3>Collaboration</h3><p>Collaboration in work transforms individual endeavors into symphonies of collective achievement. Through collaboration, diverse talents converge, fostering a rich exchange of ideas that amplifies creativity, accelerates progress, and brings forth solutions beyond what a single mind could conceive.</p></div>
    </div>
    <div class="value-head v-sky"><span class="value-num">03.</span><span class="value-name">Passion</span><span class="value-icon"><svg width="24" height="24" viewBox="0 0 24 24" fill="none" stroke="#fff" stroke-width="1.3"><path d="M12 20s-7-4-7-10a4 4 0 0 1 7-2 4 4 0 0 1 7 2c0 6-7 10-7 10z"/></svg></span></div>
    <div class="value-body" style="height:267px">
      <div class="value-art" role="img" aria-label="Illustration of a person working on a laptop beneath trees"></div>
      <div class="value-text"><h3>Passion</h3><p>Passion infuses our work with energy, transforming routine tasks into opportunities for creativity and innovation. Fueled by passion, individuals become unstoppable forces, driven to overcome challenges and achieve remarkable outcomes that benefit them and inspire those around them</p></div>
    </div>
    <div class="value-head v-yellow"><span class="value-num">04.</span><span class="value-name">Excellence</span><span class="value-icon"><svg width="24" height="24" viewBox="0 0 24 24" fill="none" stroke="#fff" stroke-width="1.3"><path d="M12 3l3 6 6 1-4.5 4 1 6L12 17l-5.5 3 1-6L3 10l6-1z"/></svg></span></div>
    <div class="value-body" style="height:267px">
      <div class="value-art" role="img" aria-label="Illustration of a rocket launch with a person holding a phone"></div>
      <div class="value-text"><h3>Excellence</h3><p>Excellence isn't a destination; it's a continuous journey of refinement and growth. Striving for excellence cultivates a culture of continuous improvement, fostering innovation, credibility, and a lasting impact that resonates far beyond the immediate task.</p></div>
    </div>
    <div class="value-head v-slate"><span class="value-num">05.</span><span class="value-name">Tenacity</span><span class="value-icon"><svg width="24" height="24" viewBox="0 0 24 24" fill="none" stroke="#fff" stroke-width="1.3"><circle cx="12" cy="12" r="7"/><path d="M12 8v4l3 2"/></svg></span></div>
    <div class="value-body" style="height:267px">
      <div class="value-art" role="img" aria-label="Illustration of two people reviewing a document with a magnifier"></div>
      <div class="value-text"><h3>Tenacity</h3><p>Tenacity is the unwavering anchor that keeps us grounded amidst adversity, propelling us forward when faced with obstacles. The resilience to persist, adapt, and learn from setbacks leads to the mastery of skills and the fulfillment of ambitious goals.</p></div>
    </div>
    <div class="value-head v-sky"><span class="value-num">06.</span><span class="value-name">Solution Mindset</span><span class="value-icon"><svg width="24" height="24" viewBox="0 0 24 24" fill="none" stroke="#fff" stroke-width="1.3"><circle cx="12" cy="10" r="5"/><path d="M10 18h4M10 21h4"/></svg></span></div>
    <div class="value-body" style="height:267px">
      <div class="value-art" role="img" aria-label="Illustration of a person holding a key beside checklist icons"></div>
      <div class="value-text"><h3>Solution Mindset</h3><p>Generosity creates a virtuous cycle of goodwill, fostering a sense of unity and shared purpose among colleagues. By freely sharing knowledge, support, and resources, we uplift those around us and contribute to a collaborative environment where collective achievements flourish.</p></div>
    </div>
    <div class="value-head v-dark"><span class="value-num">07.</span><span class="value-name">Generosity</span><span class="value-icon"><svg width="24" height="24" viewBox="0 0 24 24" fill="none" stroke="#fff" stroke-width="1.3"><rect x="5" y="10" width="14" height="10"/><path d="M4 7h16v3H4zM12 7v13"/></svg></span></div>
    <div class="value-body" style="height:267px">
      <div class="value-art" role="img" aria-label="Illustration of two colleagues fitting puzzle pieces together"></div>
      <div class="value-text"><h3>Generosity</h3><p>Generosity creates a virtuous cycle of goodwill, fostering a sense of unity and shared purpose among colleagues. By freely sharing knowledge, support, and resources, we uplift those around us and contribute to a collaborative environment where collective achievements flourish.</p></div>
    </div>
  </div>
</section>

</body>
</html>
```